Startup company business card (Media & Advertising)

we need a business card design for a company that is a startup in the media and aggregation industry. Card needs to look funky and of a new breed/modern and upmarket.

Target Market(s)

advertisers/ brand agencies & media publishers

Industry/Entity Type

Advertising

Contact Information for Business Card

Please ensure the front face signifies our brand (plintovo.com) and back has details for the contact. Standard contact such as phone , address, email , website etc.

Font styles to use
Other font styles liked:
• use styleguide and logo font and color

Colors

Designer to choose colors to be used in the design.

Requirements
Must have
• We are disrupting the media and agency industry so subtlety would be good to use imagery to signify this
Nice to have
• Please use logo colors for branding
Should not have
• be as creative and provide few options. Pick a brand color from logo and styleguide

```html
<!DOCTYPE html>
<html lang="en">
<head>
<meta charset="utf-8">
<title>Plintovo Business Card</title>
<link rel="stylesheet" href="https://fonts.googleapis.com/css2?family=Poppins:wght@400;500;600&display=swap">
<style>
  :root {
    --backdrop: #2a2a2c;
    --card-dark: #050505;
    --card-light: #ffffff;
    --brand-red: #e8384a;
    --brand-red-deep: #c22842;
    --ink: #1c1c1c;
    --ink-soft: #555555;
    --on-dark: #ffffff;
  }
  * { box-sizing: border-box; margin: 0; padding: 0; }
  html, body {
    width: 1200px;
    height: 874px;
    overflow: hidden;
    background: var(--backdrop);
    font-family: "Poppins", sans-serif;
  }
  .stage {
    position: relative;
    width: 1200px;
    height: 874px;
  }
  .card {
    position: absolute;
    left: 290px;
    width: 620px;
    height: 355px;
    overflow: hidden;
  }
  .card-front {
    top: 67px;
    background: var(--card-dark);
    display: flex;
    align-items: center;
    justify-content: center;
    gap: 22px;
  }
  .brand-dot {
    width: 54px;
    height: 54px;
    border-radius: 50%;
    background: var(--brand-red);
  }
  .brand-name {
    color: var(--on-dark);
    font-weight: 600;
    font-size: 64px;
    letter-spacing: 1px;
    line-height: 1;
  }
  .card-back {
    top: 452px;
    background: var(--card-light);
  }
  .back-accent {
    position: absolute;
    right: -70px;
    top: 40px;
    width: 340px;
    height: 340px;
  }
  .contact {
    position: absolute;
    left: 44px;
    top: 118px;
  }
  .person-name {
    color: var(--brand-red);
    font-weight: 500;
    font-size: 25px;
    line-height: 1.1;
  }
  .person-title {
    color: var(--ink);
    font-size: 15px;
    margin-bottom: 22px;
  }
  .address {
    color: var(--ink-soft);
    font-size: 16px;
    line-height: 1.35;
    margin-bottom: 8px;
    font-style: normal;
  }
  .detail-list {
    list-style: none;
    color: var(--ink-soft);
    font-size: 16px;
    line-height: 1.35;
  }
  .detail-label {
    color: var(--brand-red);
  }
</style>
</head>
<body>
  <main class="stage">
    <section class="card card-front" aria-label="Card front">
      <span class="brand-dot" aria-hidden="true"></span>
      <span class="brand-name">plintovo</span>
    </section>

    <section class="card card-back" aria-label="Card back">
      <svg class="back-accent" viewBox="0 0 340 340" aria-hidden="true">
        <circle cx="170" cy="170" r="170" fill="var(--brand-red)"/>
      </svg>
      <div class="contact">
        <h1 class="person-name">Daniel Reyes</h1>
        <p class="person-title">President</p>
        <address class="address">4120 Willow Crest Road<br>Juneau, Alaska 34512</address>
        <ul class="detail-list">
          <li><span class="detail-label">Phone:</span> 369-480-2173</li>
          <li><span class="detail-label">Email:</span> info@plintovo.com</li>
          <li><span class="detail-label">Web:</span> www.plintovo.com</li>
        </ul>
      </div>
    </section>
  </main>
</body>
</html>
```